Design a great Business Card with Logo for a Machine Learning company

I would like a business card and logo made with the help of a expert creative designer.

Company Name : Ri Vo

What is X : eXtraordinary, eXtreme, eXcess, eXcel, eXcite, eXpand

About the company : Consulting and products in Deep learning solutions for Businesses and Startups.

Company culture : We are a modern technology company where we only use state of the methods to solve customer problems. We prove our extraodinary value to our customers through State-of-the-Art solutions.

Business card requirements
---------------------------------------------
Size : Standard rectangle size
Theme : Modern but approachable(should not be intimidating, it should give a feeling of warmth and being friendly; but should look sleek and modern too)
Design : Except oval, other shapes can be used as deemed fit
Colour : Must be vibrant and should stand out from tranditional ones
Reverse Side : Should describe the services of the company creatively (Machine Learning and Deep learning solutions for IT, Retail, E-Tail, Travel, Finance, Telecom, Startups using state-of-the-art methods) - may be - text table, icons, simple text, word cloud, pictures, etc; be creative
Logo : Your design as per below requirements
Contact : Phone number, email , website(RiVo.ai) and Address (20 characters).
A very BAD design will look like this : https://www.cardolune.in/studio.aspx?template=4872153_KMB&ag=True&xnav=QRT_Design_Image&rd=1

Logo requirements
-------------------------------

Should contain Text : Ri Vo or Ri Vo A.I.
Others : Machine Learning and Deep Learning - visually incorporated into the design - this would be great to tell everything about the company just from the logo
Theme : Modern but approachable(should not be intimidating, it should give a feeling of warmth and being friendly; But should look sleek and modern too)
Design : Except oval, other shapes can be used as deemed fit. Should be a minimal design.

```html
<!DOCTYPE html>
<html lang="en">
<head>
<meta charset="utf-8">
<title>Ri Vo Business Card</title>
<link rel="stylesheet" href="https://fonts.googleapis.com/css2?family=Lato:wght@400;700;900&display=swap">
<style>
  :root {
    --bg: #e6ecea;
    --card-front: #e8633a;
    --card-back: #0b0b0b;
    --tag-red: #d8192e;
    --accent: #f6a81c;
    --ink-dark: #1a1a1a;
    --ink-light: #ffffff;
  }
  * { margin: 0; padding: 0; box-sizing: border-box; }
  html, body {
    width: 1200px; height: 800px; overflow: hidden;
    background: var(--bg);
    font-family: "Lato", Arial, sans-serif;
  }
  .canvas {
    position: relative; width: 1200px; height: 800px;
    display: flex; align-items: center; justify-content: center; gap: 40px;
  }
  .card {
    position: relative; width: 540px; height: 310px;
    border-radius: 4px;
    box-shadow: 0 10px 24px rgba(0,0,0,0.14);
    overflow: hidden;
  }
  .card--front { background: var(--card-front); color: var(--ink-dark); }
  .card--back { background: var(--card-back); color: var(--ink-light); }

  .holder { position: absolute; left: 84px; top: 30px; }
  .holder__name { font-weight: 700; font-size: 18px; letter-spacing: 0.5px; }
  .holder__title { font-size: 11.5px; letter-spacing: 0.4px; margin-top: 2px; }
  .holder__rule { width: 130px; height: 2px; background: var(--ink-dark); margin-top: 5px; }

  .contact { position: absolute; left: 56px; top: 108px; list-style: none; }
  .contact__item {
    display: flex; align-items: center; gap: 6px;
    font-size: 11px; line-height: 16px;
  }
  .contact__icon { width: 11px; height: 11px; fill: var(--ink-dark); flex: none; }

  .brand {
    position: absolute; display: flex; align-items: center; gap: 8px;
    color: var(--ink-light); font-weight: 900; letter-spacing: 1px;
  }
  .brand__mark { background: var(--accent); flex: none; }
  .card--front .brand { left: 292px; top: 122px; font-size: 60px; }
  .card--front .brand__mark { width: 16px; height: 16px; }
  .card--back .brand { left: 50%; top: 100px; transform: translateX(-50%); font-size: 62px; }
  .card--back .brand__mark { width: 16px; height: 16px; }

  .sectors {
    position: absolute; left: 44px; top: 258px;
    display: flex; gap: 7px; list-style: none;
  }
  .sectors__tag {
    background: var(--tag-red); color: var(--ink-light);
    font-size: 14px; line-height: 19px; padding: 0 9px;
  }

  .web {
    position: absolute; left: 0; right: 0; top: 226px;
    text-align: center; font-size: 12px; letter-spacing: 0.4px;
  }
</style>
</head>
<body>
<main class="canvas">
  <section class="card card--front" aria-label="Business card front">
    <div class="holder">
      <p class="holder__name">NADIA KARIM</p>
      <p class="holder__title">GRAPHICS DESIGNER</p>
      <div class="holder__rule"></div>
    </div>
    <ul class="contact">
      <li class="contact__item">
        <svg class="contact__icon" viewBox="0 0 12 12"><path d="M2.5 0.5l2 2.5-1.2 1.3c.7 1.6 2 2.9 3.4 3.6L8 6.7l2.5 2-1 2.4C5 11 1 7 0.9 2.4z"/></svg>
        01842557310
      </li>
      <li class="contact__item">
        <svg class="contact__icon" viewBox="0 0 12 12"><path d="M0.5 2h11v8h-11z M1 2.5l5 4 5-4" fill="none" stroke="#1a1a1a" stroke-width="1.2"/></svg>
        youremail.com
      </li>
      <li class="contact__item">
        <svg class="contact__icon" viewBox="0 0 12 12"><g fill="none" stroke="#1a1a1a" stroke-width="1.1"><circle cx="6" cy="6" r="5"/><ellipse cx="6" cy="6" rx="2.2" ry="5"/><path d="M1 6h10"/></g></svg>
        www.company.com
      </li>
      <li class="contact__item">
        <svg class="contact__icon" viewBox="0 0 12 12"><path d="M6 0.5a3.8 3.8 0 0 1 3.8 3.8C9.8 7 6 11.5 6 11.5S2.2 7 2.2 4.3A3.8 3.8 0 0 1 6 0.5zm0 2.2a1.6 1.6 0 1 0 0 3.2 1.6 1.6 0 0 0 0-3.2z"/></svg>
        your address
      </li>
    </ul>
    <div class="brand">
      <span class="brand__name">RI VO</span>
      <span class="brand__mark"></span>
    </div>
    <ul class="sectors">
      <li class="sectors__tag">IT</li>
      <li class="sectors__tag">Retail</li>
      <li class="sectors__tag">E-Tail</li>
      <li class="sectors__tag">Travel</li>
      <li class="sectors__tag">Finance</li>
      <li class="sectors__tag">Telecom</li>
    </ul>
  </section>

  <section class="card card--back" aria-label="Business card back">
    <div class="brand">
      <span class="brand__name">RI VO</span>
      <span class="brand__mark"></span>
    </div>
    <p class="web">www.rivo.ai</p>
  </section>
</main>
</body>
</html>
```